Business Cards

Need a neat design for a new business card

Industry/Entity Type

Residential Construction

Contact Information for Business Card

Company Name- KOVE Construction Inc.
Owner- Marcus Tolliver
Phone number- (555)203-7481
Email- kovecohomes@brindlemail.example
Facebook- www.socialpage.example/kovecohomes

Colors
fefdec

```html
<!DOCTYPE html>
<html lang="en">
<head>
<meta charset="utf-8">
<title>KOVE Construction Inc. – Business Card</title>
<link rel="stylesheet" href="https://fonts.googleapis.com/css2?family=Philosopher:wght@400&family=Roboto:wght@400&display=swap">
<style>
  :root {
    --backdrop: #b4b4b4;
    --card-dark: #0a0a0a;
    --card-light: #fefdec;
    --ink-light: #eeecd4;
    --ink-dark: #151515;
    --shadow: rgba(0, 0, 0, 0.28);
  }
  * { margin: 0; padding: 0; box-sizing: border-box; }
  html, body {
    width: 1200px;
    height: 576px;
    overflow: hidden;
    background: var(--backdrop);
  }
  .canvas {
    position: relative;
    width: 1200px;
    height: 576px;
  }
  .card {
    position: absolute;
    top: 138px;
    width: 484px;
    height: 294px;
    border-radius: 12px;
    box-shadow: 2px 3px 6px var(--shadow);
  }
  .card-front {
    left: 82px;
    background: var(--card-dark);
    display: flex;
    align-items: center;
    justify-content: center;
  }
  .card-back {
    left: 602px;
    background: var(--card-light);
    color: var(--ink-dark);
  }
  .brand-name {
    font-family: 'Philosopher', sans-serif;
    font-weight: 400;
    white-space: nowrap;
  }
  .card-front .brand-name {
    color: var(--ink-light);
    font-size: 36px;
    letter-spacing: 1px;
  }
  .card-back .brand-name {
    position: absolute;
    left: 304px;
    width: 140px;
    bottom: 40px;
    font-size: 22px;
    line-height: 1.15;
    text-align: center;
    white-space: normal;
    color: var(--ink-dark);
  }
  .brand-line { display: block; }
  .holder {
    position: absolute;
    left: 30px;
    top: 28px;
  }
  .holder-name {
    font-family: 'Philosopher', sans-serif;
    font-size: 21px;
    font-weight: 400;
    line-height: 1.2;
  }
  .holder-title {
    font-family: 'Roboto', sans-serif;
    font-size: 12px;
    margin-top: 2px;
  }
  .contact-list {
    position: absolute;
    left: 30px;
    top: 206px;
    list-style: none;
    font-family: 'Roboto', sans-serif;
    font-size: 13px;
  }
  .contact-item {
    display: flex;
    align-items: center;
    height: 18.5px;
    white-space: nowrap;
  }
  .contact-icon {
    width: 12px;
    height: 12px;
    margin-right: 10px;
    flex: none;
  }
  .social-mark {
    width: 10px;
    height: 10px;
    margin: 0 12px 0 1px;
    background: var(--ink-dark);
    border-radius: 2px;
    flex: none;
  }
</style>
</head>
<body>
<main class="canvas">
  <section class="card card-front" aria-label="Card front">
    <p class="brand-name">KOVE Construction</p>
  </section>

  <section class="card card-back" aria-label="Card back">
    <div class="holder">
      <h1 class="holder-name">Marcus Tolliver</h1>
      <p class="holder-title">Managing Director</p>
    </div>

    <ul class="contact-list">
      <li class="contact-item">
        <svg class="contact-icon" viewBox="0 0 12 12" aria-hidden="true">
          <path d="M1 4 Q6 0 11 4 L10 5.5 L8 5 L8 4 Q6 3 4 4 L4 5 L2 5.5 Z" fill="#151515"/>
          <rect x="2.5" y="6" width="7" height="5" rx="1" fill="#151515"/>
        </svg>
        <span>(555)203-7481</span>
      </li>
      <li class="contact-item">
        <span class="social-mark" aria-hidden="true"></span>
        <span>/kovecohomes</span>
      </li>
      <li class="contact-item">
        <svg class="contact-icon" viewBox="0 0 12 12" aria-hidden="true">
          <rect x="0.5" y="2.5" width="11" height="7.5" fill="#151515"/>
          <path d="M0.8 3 L6 7 L11.2 3" fill="none" stroke="#fefdec" stroke-width="1"/>
        </svg>
        <span>kovecohomes@brindlemail.example</span>
      </li>
    </ul>

    <p class="brand-name"><span class="brand-line">KOVE</span><span class="brand-line">Construction</span></p>
  </section>
</main>
</body>
</html>
```